Career Counselor in need of a business card design

Hello Creatives! I'm in need of a business card design for a new company based in Georgia, USA called Pathways By Lumen.

Some things that may be helpful in creating your concept(s) include:

My Logo (Included in the Files section): There are three versions, two versions are in the second file. The all gold stacked (vertical) version is my primary logo and then there are two horizontal versions (one is all gold and the other is gold and grey).

My mission: to empower tweens through young adults to realize and actualize their CAREER ASPIRATIONS.
My vision: for tweens through young adults to LIVE LIFE ON PURPOSE and become CONTRIBUTING MEMBERS OF SOCIETY.

Biblical scriptures that support my ‘Why’: Psalms 127: 3-4(NIV) Children are a heritage from the Lord, offspring a reward from him. Like ARROWS in the hands of a warrior are children…. And Proverbs 29:18(JKV) Where there is no VISION, the people perish.

*Words in ALL CAPS are to emphasize what's important to me and may possibly provide you some inspiration (IDK - Have fun with it)!

Target Market(s)

My ideal customers are parents, guardians, and young adults.

Contact Information for Business Card

My name, degrees and credential: Delmira Fosket, M.S., Ed.S., NCC
Title: College and Career Coach and Consultant

Number: 555.317.8842
Address: 2618 Velbrook Avenue., Suite 407, Brinwood, OK 73199
Email: info@pathwaysbylumen.co
Website: www.pathwaysbylumen.co

My population: TWEENS • TEENS • EMERGING ADULTS
Services offered: One-On-One Sessions • Small Groups • Workshops

Colors

Designer to choose colors to be used in the design.

Requirements
Nice to have
• Either my mission or vision but I will understand if it does not all fit.
• My mission: To empower tweens through young adults to realize and actualize their career aspirations.
• My vision: For tweens through young adults to live life on purpose and become contributing members of society.

```html
<!DOCTYPE html>
<html lang="en">
<head>
<meta charset="utf-8">
<title>Pathways By Lumen — Business Card</title>
<link rel="stylesheet" href="https://fonts.googleapis.com/css2?family=Cinzel:wght@600&family=Tinos:wght@700&family=Fira+Sans:wght@400&display=swap">
<style>
  :root {
    --backdrop: #3a3a3b;
    --card: #111112;
    --gold: #d8ac2c;
    --grey: #a9a9a9;
    --ghost: rgba(216, 172, 44, 0.07);
  }
  * { margin: 0; padding: 0; box-sizing: border-box; }
  html, body { width: 1200px; height: 900px; overflow: hidden; }
  body {
    background: var(--backdrop);
    position: relative;
    font-family: "Fira Sans", sans-serif;
    color: var(--grey);
  }
  .card {
    position: absolute;
    left: 250px;
    width: 700px;
    height: 400px;
    background: var(--card);
    overflow: hidden;
  }
  .card--services { top: 35px; }
  .card--contact { top: 465px; }

  .ghost-ring {
    position: absolute;
    border: 22px solid var(--ghost);
    border-radius: 50%;
  }
  .card--services .ghost-ring { width: 320px; height: 320px; left: 400px; top: 70px; }
  .card--contact .ghost-ring { width: 340px; height: 340px; left: 380px; top: 95px; }

  .brand {
    position: absolute;
    display: flex;
    align-items: center;
    gap: 18px;
  }
  .brand__dot {
    border: 3px solid var(--gold);
    border-radius: 50%;
    flex: none;
  }
  .brand__name {
    font-family: "Cinzel", serif;
    font-weight: 600;
    color: var(--gold);
    line-height: 1;
  }
  .brand__name span { display: block; }
  .card--services .brand { left: 36px; top: 30px; }
  .card--services .brand__dot { width: 70px; height: 70px; }
  .card--services .brand__name .line-1 { font-size: 40px; }
  .card--services .brand__name .line-2 { font-size: 20px; letter-spacing: 7px; margin-top: 4px; }

  .card--contact .brand { left: 40px; top: 120px; }
  .card--contact .brand__dot { width: 100px; height: 100px; }
  .card--contact .brand__name .line-1 { font-size: 54px; }
  .card--contact .brand__name .line-2 { font-size: 26px; letter-spacing: 10px; margin-top: 6px; }

  .dot { color: var(--gold); margin: 0 6px; }

  .audience {
    position: absolute;
    left: 40px; top: 140px;
    font-size: 15px;
    letter-spacing: 0.5px;
  }
  .services {
    position: absolute;
    left: 40px; top: 205px;
    width: 360px;
  }
  .services__title {
    font-family: "Cinzel", serif;
    font-weight: 600;
    font-size: 19px;
    letter-spacing: 1px;
    padding: 6px 0 4px;
    border-top: 1.5px solid var(--gold);
    border-bottom: 1.5px solid var(--gold);
    width: 260px;
  }
  .services__list {
    margin-top: 12px;
    font-size: 16px;
    white-space: nowrap;
  }

  .person {
    position: absolute;
    right: 36px; top: 34px;
    text-align: right;
  }
  .person__name {
    font-family: "Tinos", serif;
    font-weight: 700;
    font-size: 24px;
    color: var(--gold);
    white-space: nowrap;
  }
  .person__title { font-size: 17px; margin-top: 6px; white-space: nowrap; }

  .contact {
    position: absolute;
    left: 50px; top: 255px;
    border-left: 2px solid var(--gold);
    padding-left: 18px;
    list-style: none;
    font-size: 16px;
  }
  .contact li { display: flex; align-items: center; gap: 10px; height: 24px; white-space: nowrap; }
  .contact svg { width: 15px; height: 15px; fill: var(--gold); flex: none; }
  .address {
    position: absolute;
    left: 50px; top: 342px;
    font-size: 16px;
    white-space: nowrap;
  }
</style>
</head>
<body>
  <section class="card card--services">
    <div class="ghost-ring" aria-hidden="true"></div>
    <div class="brand">
      <div class="brand__dot"></div>
      <div class="brand__name"><span class="line-1">PATHWAYS</span><span class="line-2">BY LUMEN</span></div>
    </div>
    <p class="audience">TWEENS<span class="dot">•</span>TEENS<span class="dot">•</span>EMERGING ADULTS</p>
    <div class="services">
      <h2 class="services__title">SERVICES OFFERED</h2>
      <p class="services__list">One-On-One Sessions<span class="dot">•</span>Small Groups<span class="dot">•</span>Workshops</p>
    </div>
  </section>

  <section class="card card--contact">
    <div class="ghost-ring" aria-hidden="true"></div>
    <div class="person">
      <h1 class="person__name">Delmira Fosket, M.S., Ed.S., NCC</h1>
      <p class="person__title">College and Career Coach and Consultant</p>
    </div>
    <div class="brand">
      <div class="brand__dot"></div>
      <div class="brand__name"><span class="line-1">PATHWAYS</span><span class="line-2">BY LUMEN</span></div>
    </div>
    <ul class="contact">
      <li>
        <svg viewBox="0 0 24 24" aria-hidden="true"><path d="M6.6 10.8a15.1 15.1 0 0 0 6.6 6.6l2.2-2.2c.3-.3.7-.4 1-.2 1.1.4 2.3.6 3.6.6.6 0 1 .4 1 1V20c0 .6-.4 1-1 1A17 17 0 0 1 3 4c0-.6.4-1 1-1h3.5c.6 0 1 .4 1 1 0 1.3.2 2.5.6 3.6.1.3 0 .7-.2 1z"/></svg>
        555.317.8842
      </li>
      <li>
        <svg viewBox="0 0 24 24" aria-hidden="true"><path d="M2 5h20v14H2zm2 2v.5l8 5 8-5V7zm0 2.8V17h16V9.8l-8 5z"/></svg>
        info@pathwaysbylumen.co
      </li>
      <li>
        <svg viewBox="0 0 24 24" aria-hidden="true"><path d="M12 2a10 10 0 1 0 0 20 10 10 0 0 0 0-20zm0 2c.9 0 2.2 2 2.6 5H9.4C9.8 6 11.1 4 12 4zm-7.7 5a8 8 0 0 1 4.6-4.4C8.2 5.9 7.600 7.4 7.4 9zm0 6h3.1c.2 1.6.8 3.1 1.5 4.4A8 8 0 0 1 4.3 15zm5.1 0h5.2c-.4 3-1.7 5-2.6 5s-2.2-2-2.6-5zm0-2a16 16 0 0 1 0-2h5.2a16 16 0 0 1 0 2zm7.2 2h3.1a8 8 0 0 1-4.6 4.4c.7-1.3 1.3-2.8 1.5-4.4zm0-6c-.2-1.6-.8-3.1-1.5-4.4A8 8 0 0 1 19.7 9z"/></svg>
        www.pathwaysbylumen.co
      </li>
    </ul>
    <p class="address">2618 Velbrook Avenue., Suite 407, Brinwood, OK 73199</p>
  </section>
</body>
</html>
```